Far Hollow Laugh Circuit needs an awesome new show poster

The Far Hollow Laugh Circuit is a comedy show for theatres featuring comics from the South (US) who live up North. We need a new flyer/poster to send to buyers for next year's season. We are attaching old flyers - but the new one does NOT have to look like them.
.
Be creative! We are open to all ideas! Think about what makes people interested in buying a ticket to a live comedy performance. The design could be artistic (like a fernbrook music poster) or just very funny. It should in some way represent the American South.

Let us know if you have any questions.
Thanks!
Dana & Rod
Updates

Project Deadline Extended
Reason: One of our decision makers has to have unexpected surgery this week so we are extending the deadline so that he Will be able to review all the entries. Thanks

Project Deadline Extended

Project Deadline Extended

Target Market(s)

Theater audiences ages 30+, men and women,

Industry/Entity Type

Tour

Requirements
Must have
• show name - Far Hollow Laugh
artists' names - Rod Castell & Dana Prewitt (Rod Castell's name should come first)
Nice to have
• logos or list of TV credits (as seen on the older versions)
representations of the South
Should not have
• no typical stand-up comedy icons or design, like microphones, spotlights, etc.
please do not use the old square logo (but feel free to come up with a new one)

```html
<!DOCTYPE html>
<html lang="en">
<head>
<meta charset="utf-8">
<title>Far Hollow Laugh — Rod Castell &amp; Dana Prewitt</title>
<link rel="stylesheet" href="https://fonts.googleapis.com/css2?family=Poppins:wght@500;700&family=Arimo:wght@400&display=swap">
<style>
  :root {
    --page: #c9c9c9;
    --ink: #000000;
    --yellow: #ffd400;
    --white: #ffffff;
    --red-dark: #5a0000;
    --red: #a30a05;
    --strip-top: #f4f4f4;
    --strip-bottom: #dcdcdc;
    --credit: #1d1d1d;
  }
  html, body {
    margin: 0;
    width: 940px;
    height: 1200px;
    overflow: hidden;
    background: var(--page);
  }
  .poster {
    position: absolute;
    left: 44px;
    top: 48px;
    width: 854px;
    height: 1105px;
    background: var(--ink);
    outline: 1px solid #555;
    overflow: hidden;
  }
  .chevrons { position: absolute; left: 0; top: 0; }
  .portrait {
    position: absolute;
    top: 0;
    height: 780px;
  }
  .portrait--rod {
    left: 156px;
    width: 269px;
    background: linear-gradient(180deg, #3a3a3a 0%, #b0907a 22%, #c98e6c 38%, #2a2a2a 52%, #d4421c 62%, #1a1a1a 88%, #000 100%);
  }
  .portrait--dana {
    left: 425px;
    width: 273px;
    background: linear-gradient(180deg, #c9b494 0%, #d9b48e 25%, #c99a80 40%, #a8b6b8 60%, #6e7f86 80%, #000 100%);
  }
  .show-title {
    position: absolute;
    left: 0;
    width: 100%;
    margin: 0;
    font-family: "Poppins", sans-serif;
    font-weight: 500;
    text-align: center;
    line-height: 1;
    letter-spacing: -2px;
  }
  .show-title span { position: absolute; left: 0; width: 100%; }
  .show-title .line-1 { top: 355px; font-size: 168px; color: var(--yellow); letter-spacing: -6px; }
  .show-title .line-2 { top: 527px; font-size: 128px; color: var(--white); }
  .show-title .line-3 { top: 650px; font-size: 128px; color: var(--yellow); }
  .artists {
    position: absolute;
    top: 790px;
    left: 0;
    width: 100%;
    margin: 0;
    text-align: center;
    font-family: "Arimo", sans-serif;
    font-size: 44px;
    color: var(--white);
  }
  .credits {
    position: absolute;
    left: 0;
    top: 901px;
    width: 100%;
    height: 204px;
    background: linear-gradient(180deg, var(--strip-top), var(--strip-bottom));
    list-style: none;
    margin: 0;
    padding: 0;
  }
  .credit {
    position: absolute;
    font-family: "Poppins", sans-serif;
    font-weight: 700;
    color: var(--credit);
    line-height: 1;
    white-space: nowrap;
    display: flex;
    align-items: center;
    gap: 6px;
  }
  .credit .dot {
    width: 14px; height: 14px; border-radius: 50%; background: var(--credit);
  }
</style>
</head>
<body>
  <main class="poster">
    <svg class="chevrons" width="854" height="780" viewBox="0 0 854 780" aria-hidden="true">
      <defs>
        <linearGradient id="bandLeft" x1="0" x2="1">
          <stop offset="0" stop-color="var(--red)"/>
          <stop offset="1" stop-color="var(--red-dark)"/>
        </linearGradient>
        <linearGradient id="bandRight" x1="1" x2="0">
          <stop offset="0" stop-color="var(--red)"/>
          <stop offset="1" stop-color="var(--red-dark)"/>
        </linearGradient>
      </defs>
      <polygon points="0,360 160,470 160,650 0,600" fill="url(#bandLeft)"/>
      <polygon points="854,380 698,500 698,650 854,610" fill="url(#bandRight)"/>
    </svg>

    <div class="portrait portrait--rod" role="img" aria-label="Portrait photo of Rod Castell smiling, grey hair, orange shirt and dark jacket"></div>
    <div class="portrait portrait--dana" role="img" aria-label="Portrait photo of Dana Prewitt laughing, blonde hair, light floral top"></div>

    <h1 class="show-title">
      <span class="line-1">FAR</span>
      <span class="line-2">HOLLOW</span>
      <span class="line-3">LAUGH</span>
    </h1>
    <p class="artists">Rod Castell &amp; Dana Prewitt</p>

    <ul class="credits" aria-label="As seen on">
      <li class="credit" style="left:20px; top:54px; font-size:22px;"><span class="dot"></span>Jest Channel</li>
      <li class="credit" style="left:150px; top:100px; font-size:34px;">KidParent</li>
      <li class="credit" style="left:402px; top:38px; font-size:22px; flex-direction:column; align-items:flex-start; gap:2px;">Late<br>Lantern<br>Hour</li>
      <li class="credit" style="left:532px; top:60px; font-size:44px;">HVX</li>
      <li class="credit" style="left:676px; top:52px; font-size:40px;"><span class="dot"></span>Brisa</li>
      <li class="credit" style="left:28px; top:142px; font-size:20px;">Orbit Radio</li>
      <li class="credit" style="left:196px; top:142px; font-size:20px;">Trailhand</li>
      <li class="credit" style="left:130px; top:172px; font-size:18px;">Plains Network</li>
      <li class="credit" style="left:298px; top:158px; font-size:24px;">TuneOne</li>
      <li class="credit" style="left:500px; top:152px; font-size:24px;">Night Desk Show</li>
      <li class="credit" style="left:716px; top:130px; font-size:46px;">CRV</li>
    </ul>
  </main>
</body>
</html>
```